Unique, Impressive, and Modern Business Card

Looking for a distinctive, unique business card. We are distributors of tire repairs supplies, tools, machinery, and chemicals. Our target market are tire repair shops, tire franchises, and mechanic shops. We would like our design to include tire characteristics, and use our business colors. Feel free to use all types design and printing options (emboss, spot uv, foil, etc) QR code may be applied, you can use different size business cards ( standard, square, rounded edge, colored edge, etc), all formats needed for printing, also editable for future changes

Target Market(s)

Automotive, Tire industries

Industry/Entity Type

Tire Industry (automotive)

Contact Information for Business Card

Business logo, business Name (Corvane Supply Inc), Name (Marcus Pellow), Position (President) Address (58 Fernhollow Lane, Brentwood NY 11742), Contact number (Company 1-855-302-4418, Cell 1-631-245-9073, email address (marcus.pellow@corvanesupply.com), URL (www.corvanesupply.com

Requirements
Must have
• Must include Business Colors (Black, Green, Blue, White) see sample website file
Nice to have
• emboss, spot uv, etc

```html
<!DOCTYPE html>
<html lang="en">
<head>
<meta charset="utf-8">
<title>Corvane Supply Inc — Business Card</title>
<link rel="stylesheet" href="https://fonts.googleapis.com/css2?family=Montserrat:wght@400;500;700&display=swap">
<style>
  :root {
    --backdrop: #d3d1d2;
    --card-blue: #3a4b9c;
    --mark-blue: #2e3d85;
    --accent-green: #4fba45;
    --text-white: #ffffff;
  }
  * { box-sizing: border-box; margin: 0; padding: 0; }
  html, body {
    width: 1084px;
    height: 1200px;
    overflow: hidden;
    background: var(--backdrop);
    font-family: "Montserrat", Arial, sans-serif;
  }
  .canvas { position: relative; width: 1084px; height: 1200px; }
  .card {
    position: absolute;
    left: 202px;
    width: 680px;
    height: 389px;
    background: var(--card-blue);
    overflow: hidden;
  }
  .card--front { top: 129px; }
  .card--back { top: 681px; }

  .brand {
    position: absolute;
    display: flex;
    align-items: center;
    color: var(--mark-blue);
    font-weight: 500;
    white-space: nowrap;
  }
  .brand__dot { border-radius: 50%; background: var(--mark-blue); flex: none; }
  .brand--front { left: 0; right: 0; top: 163px; justify-content: center; font-size: 34px; letter-spacing: 2px; gap: 18px; }
  .brand--front .brand__dot { width: 60px; height: 60px; }
  .brand--back { left: 52px; top: 52px; font-size: 20px; letter-spacing: 1px; gap: 12px; }
  .brand--back .brand__dot { width: 40px; height: 40px; }

  .front__url {
    position: absolute;
    left: 0; right: 0; top: 326px;
    text-align: center;
    color: var(--text-white);
    font-size: 14px;
    font-weight: 500;
    letter-spacing: 1.6px;
  }

  .person { position: absolute; left: 355px; top: 44px; }
  .person__name {
    color: var(--accent-green);
    font-size: 29px;
    font-weight: 700;
    letter-spacing: 3.5px;
    line-height: 1.1;
  }
  .person__title {
    color: var(--text-white);
    font-size: 17px;
    font-weight: 500;
    letter-spacing: 1.8px;
    margin-top: 2px;
  }

  .address {
    position: absolute;
    left: 356px; top: 171px;
    color: var(--text-white);
    font-size: 12.5px;
    font-weight: 500;
    letter-spacing: 1.3px;
    line-height: 15px;
  }

  .contacts { position: absolute; left: 356px; top: 216px; list-style: none; }
  .contacts__item {
    display: flex;
    align-items: center;
    height: 22px;
    color: var(--text-white);
    font-size: 12.5px;
    font-weight: 500;
    letter-spacing: 1.3px;
  }
  .contacts__icon { width: 17px; height: 17px; margin-right: 10px; flex: none; }
  .contacts__accent { color: var(--accent-green); }
</style>
</head>
<body>
<main class="canvas">

  <section class="card card--front" aria-label="Card front">
    <div class="brand brand--front">
      <span class="brand__dot"></span>
      <span class="brand__name">CORVANE SUPPLY</span>
    </div>
    <p class="front__url">www.corvanesupply.com</p>
  </section>

  <section class="card card--back" aria-label="Card back">
    <div class="brand brand--back">
      <span class="brand__dot"></span>
      <span class="brand__name">CORVANE SUPPLY</span>
    </div>

    <div class="person">
      <h1 class="person__name">Marcus Pellow</h1>
      <p class="person__title">President</p>
    </div>

    <address class="address" style="font-style:normal">
      58 Fernhollow Lane,<br>Brentwood NY 11742
    </address>

    <ul class="contacts">
      <li class="contacts__item">
        <svg class="contacts__icon" viewBox="0 0 24 24" aria-hidden="true">
          <path fill="var(--accent-green)" d="M6.6 10.8a15.1 15.1 0 0 0 6.6 6.6l2.2-2.2a1 1 0 0 1 1-.25 11.4 11.4 0 0 0 3.6.57 1 1 0 0 1 1 1V20a1 1 0 0 1-1 1A17 17 0 0 1 3 4a1 1 0 0 1 1-1h3.5a1 1 0 0 1 1 1c0 1.25.2 2.45.57 3.6a1 1 0 0 1-.25 1z"/>
        </svg>
        1-631-245-9073
      </li>
      <li class="contacts__item">
        <svg class="contacts__icon" viewBox="0 0 24 24" aria-hidden="true">
          <path fill="var(--accent-green)" d="M2 8c0-2 4-4 10-4s10 2 10 4v2h-5V8H7v2H2zM6 11h12l2 9H4zm4 2v2h4v-2zm0 3v2h4v-2z"/>
        </svg>
        1-855-302-4418
      </li>
      <li class="contacts__item">
        <svg class="contacts__icon" viewBox="0 0 24 24" aria-hidden="true">
          <rect x="2" y="5" width="20" height="14" fill="var(--accent-green)"/>
          <path d="M2 5l10 8 10-8M2 19l8-7M22 19l-8-7" fill="none" stroke="var(--card-blue)" stroke-width="1.5"/>
        </svg>
        marcus.pellow@corvanesupply.com
      </li>
      <li class="contacts__item">
        <svg class="contacts__icon" viewBox="0 0 24 24" aria-hidden="true">
          <g fill="none" stroke="var(--accent-green)" stroke-width="2">
            <circle cx="12" cy="12" r="10"/>
            <ellipse cx="12" cy="12" rx="4.5" ry="10"/>
            <path d="M2 12h20M4 7h16M4 17h16"/>
          </g>
        </svg>
        <span>www.<span class="contacts__accent">corvanesupply</span>.com</span>
      </li>
    </ul>
  </section>

</main>
</body>
</html>
```